Wedding Dried Apple Label / Name Place Card

We are looking for a simple but stylish label to be attached via string to a bag of dried apples from my family's fruit farm. The size of the label we think should be similar to the size of a business card. The packaging will be a plastic bag: 4" x 2" x 6".
We would like it to say something like:
Corin & Tessa
Est. Sept 10, 2017
Dried Apple Slices
Product of Marrow Orchard Farm
________________
(We need a spot to write in the name of the person and a table number)
Our colors are also grey and navy, and would like these colors to be used.
We have uploaded a photo of the plastic bag.

```html
<!DOCTYPE html>
<html lang="en">
<head>
<meta charset="UTF-8">
<title>Marrow Orchard Farm – Dried Apple Slices Label</title>
<link rel="stylesheet" href="https://fonts.googleapis.com/css2?family=Lobster&family=Lobster+Two:ital,wght@1,400&family=Philosopher&display=swap">
<style>
  :root {
    --navy: #2b0f8e;
    --grey-dark: #8a8a8a;
    --grey-mid: #bcbcbc;
    --grey-light: #e6e6e6;
    --paper: #ffffff;
    --backdrop: #eeeeee;
    --ink: #3a3a3a;
  }
  * { margin: 0; padding: 0; box-sizing: border-box; }
  html, body {
    width: 1200px;
    height: 881px;
    overflow: hidden;
    background: linear-gradient(160deg, #f7f7f7 0%, var(--backdrop) 100%);
  }
  .label-card {
    position: absolute;
    left: 408px;
    top: 173px;
    width: 384px;
    height: 534px;
    background: var(--paper);
    box-shadow: 4px 6px 10px rgba(0,0,0,0.22);
    overflow: hidden;
  }
  .mandala-area {
    position: absolute;
    left: -20px;
    top: -200px;
    width: 424px;
    height: 448px;
    border-radius: 50%;
    background: radial-gradient(circle at 50% 50%,
      var(--grey-mid) 0%, var(--grey-light) 30%, #f1f1f1 55%, var(--grey-light) 80%, #f6f6f6 100%);
  }
  .farm-name {
    position: absolute;
    left: 0;
    width: 100%;
    top: 108px;
    text-align: center;
    font-family: "Lobster", cursive;
    font-weight: 400;
    color: var(--navy);
  }
  .farm-name-main {
    display: block;
    font-size: 64px;
    line-height: 70px;
  }
  .farm-name-sub {
    display: block;
    font-size: 34px;
    line-height: 40px;
  }
  .product-banner {
    position: absolute;
    left: 44px;
    top: 291px;
    width: 296px;
    height: 56px;
  }
  .product-banner svg { position: absolute; inset: 0; }
  .product-name {
    position: absolute;
    inset: 0;
    display: flex;
    align-items: center;
    justify-content: center;
    font-family: "Lobster Two", cursive;
    font-style: italic;
    color: #ffffff;
    font-size: 26px;
  }
  .divider {
    position: absolute;
    left: 42px;
    width: 300px;
    height: 26px;
  }
  .divider-top { top: 352px; }
  .divider-bottom { top: 458px; }
  .divider-rule {
    position: absolute;
    left: 0;
    right: 0;
    height: 2px;
    background: var(--grey-dark);
  }
  .divider-top .divider-rule { bottom: 0; }
  .divider-bottom .divider-rule { top: 0; }
  .divider-flourish {
    position: absolute;
    left: 40px;
    right: 40px;
    height: 10px;
    border-radius: 5px;
    background: linear-gradient(90deg, rgba(188,188,188,0) 0%, var(--grey-mid) 30%, var(--grey-dark) 50%, var(--grey-mid) 70%, rgba(188,188,188,0) 100%);
  }
  .divider-top .divider-flourish { top: 4px; }
  .divider-bottom .divider-flourish { bottom: 4px; }
  .couple-details {
    position: absolute;
    left: 0;
    width: 100%;
    top: 388px;
    text-align: center;
    font-family: "Philosopher", sans-serif;
    color: var(--ink);
    font-size: 22px;
    line-height: 28px;
  }
  .write-in {
    position: absolute;
    left: 42px;
    width: 300px;
    top: 508px;
    height: 2px;
    display: flex;
    gap: 20px;
  }
  .write-in-guest { flex: 1; border-bottom: 1.5px solid var(--grey-mid); }
  .write-in-table { width: 60px; border-bottom: 1.5px solid var(--grey-mid); }
</style>
</head>
<body>
  <main class="label-card">
    <div class="mandala-area" role="img" aria-label="Grey circular mandala pattern across the top of the label"></div>

    <h1 class="farm-name">
      <span class="farm-name-main">Marrow</span>
      <span class="farm-name-sub">Orchard Farm</span>
    </h1>

    <div class="product-banner">
      <svg viewBox="0 0 296 56" width="296" height="56" aria-hidden="true">
        <polygon points="0,3 296,3 284,28 296,53 0,53 12,28" fill="var(--navy)"/>
        <polygon points="6,8 290,8 279,28 290,48 6,48 17,28" fill="none" stroke="#ffffff" stroke-width="1" opacity="0.55"/>
      </svg>
      <div class="product-name">Dried Apple Slices</div>
    </div>

    <div class="divider divider-top">
      <div class="divider-flourish" role="img" aria-label="Grey scroll flourish ornament"></div>
      <div class="divider-rule"></div>
    </div>

    <p class="couple-details">Corin &amp; Tessa<br>Est. Sept 10, 2017</p>

    <div class="divider divider-bottom">
      <div class="divider-rule"></div>
      <div class="divider-flourish" role="img" aria-label="Grey scroll flourish ornament"></div>
    </div>

    <div class="write-in">
      <span class="write-in-guest" aria-label="Write-in line for guest name"></span>
      <span class="write-in-table" aria-label="Write-in line for table number"></span>
    </div>
  </main>
</body>
</html>
```